Business Card Design Project : Tidewell Press

In preparation for market launch, Whistler's Tidewell Press require the development of a business card. Tidewell Press is a Community online publishing web portal. We provide the the city of Whistler located in B.C. (Canada) business directories, News, Classified ads, News, Events and blogs etc.

The main focus of the brand is to help local businesses to corporate with their online advertisement and marketing. Meeting our clients face to face is a must (B2B).

Target Market(s)

The target market is B2B customers. Business Owners to Marketing, advertising Managers

Industry/Entity Type

Business

Requirements
Must have
• - The business card will be two sided.
the BACK side will have our logo which consist of (icon, url,slogan) submited. The logo will be middle and centred.

The FRONT side should have company details:

Company Legal Name: FERNDALE TIDEWELL PRESS

Owen Marsk
Director of Sales & Marketing

www.ferndaletidewell.biz
owen@ferndaletidewell.biz

Phone: 555 014 3826
#2817 - 562 E. Harlow Ave.
Vancouver, B.C. K7P2R4 Canada
Nice to have
• - For the "FRONT" side of our business card. You can separate or re-arrange with our logo components (icon, logo,slogan). It does not have to be together.

Also our company legal name is rather long so arrange or organize the name in a way to make it shorter. Your experience and creativity will have to come in play.
Should not have
• should not have other colors beside logo color and black text (2 colors). Also nothing Three dimensional

```html
<!DOCTYPE html>
<html lang="en">
<head>
<meta charset="utf-8">
<title>Ferndale Tidewell Press — Business Card</title>
<link rel="stylesheet" href="https://fonts.googleapis.com/css2?family=Arimo:wght@400;700&family=Open+Sans:wght@400;700&display=swap">
<style>
  :root {
    --ink: #000000;
    --brand-blue: #0a78cc;
    --paper: #ffffff;
    --text-dark: #222222;
    --canvas: #ffffff;
  }
  * { margin: 0; padding: 0; box-sizing: border-box; }
  html, body {
    width: 1200px;
    height: 900px;
    overflow: hidden;
    background: var(--canvas);
  }
  .canvas {
    position: relative;
    width: 1200px;
    height: 900px;
  }
  .card {
    position: absolute;
    left: 281px;
    width: 649px;
    height: 369px;
    overflow: hidden;
  }

  /* Back side */
  .card-back {
    top: 59px;
    background: var(--ink);
    font-family: "Open Sans", Arial, sans-serif;
    color: var(--paper);
    text-align: center;
  }
  .back-brand {
    position: absolute;
    top: 120px;
    left: 0;
    width: 100%;
    display: flex;
    justify-content: center;
    align-items: center;
    gap: 14px;
  }
  .brand-square {
    width: 30px;
    height: 30px;
    background: var(--brand-blue);
  }
  .brand-name {
    font-family: "Arimo", Arial, sans-serif;
    font-weight: 700;
    font-size: 46px;
    color: var(--brand-blue);
    letter-spacing: 0.5px;
  }
  .back-url {
    position: absolute;
    top: 209px;
    left: 0;
    width: 100%;
    font-weight: 700;
    font-size: 28px;
    letter-spacing: -0.3px;
  }
  .back-slogan {
    position: absolute;
    top: 247px;
    left: 0;
    width: 100%;
    font-size: 19px;
  }

  /* Front side */
  .card-front {
    top: 480px;
    background: var(--paper);
    font-family: "Arimo", Arial, sans-serif;
  }
  .front-shapes {
    position: absolute;
    inset: 0;
    width: 100%;
    height: 100%;
  }
  .shape-dark { fill: var(--ink); }
  .shape-blue { fill: var(--brand-blue); }

  .company {
    position: absolute;
    right: 29px;
    top: 14px;
    text-align: right;
    color: var(--paper);
    font-weight: 700;
    line-height: 1;
  }
  .company-line1 {
    display: block;
    font-size: 35px;
    letter-spacing: 1.5px;
  }
  .company-line2 {
    display: block;
    font-size: 20px;
    margin-top: 4px;
    letter-spacing: 0.3px;
  }

  .person {
    position: absolute;
    left: 136px;
    top: 137px;
    line-height: 1;
  }
  .person-name {
    font-size: 24px;
    font-weight: 700;
    color: var(--ink);
  }
  .person-title {
    font-size: 17px;
    color: var(--brand-blue);
    margin-top: 6px;
  }
  .person-links {
    position: absolute;
    left: 136px;
    top: 196px;
    font-size: 16px;
    line-height: 22px;
    color: var(--text-dark);
    list-style: none;
  }

  .contact {
    position: absolute;
    right: 29px;
    top: 282px;
    text-align: right;
    color: var(--paper);
    font-size: 17px;
    line-height: 22px;
    font-style: normal;
  }
</style>
</head>
<body>
<main class="canvas">

  <section class="card card-back" aria-label="Card back">
    <div class="back-brand">
      <span class="brand-square"></span>
      <span class="brand-name">Tidewell Press</span>
    </div>
    <p class="back-url">www.ferndaletidewell.biz</p>
    <p class="back-slogan">Your information gateway</p>
  </section>

  <section class="card card-front" aria-label="Card front">
    <svg class="front-shapes" viewBox="0 0 415 236" preserveAspectRatio="none" aria-hidden="true">
      <path class="shape-dark" d="M0,0 H415 V72 C402,62 385,53 365,54 C335,56 322,92 290,92 C258,92 242,62 218,36 C198,15 178,5 157,7 C132,10 116,38 96,64 C66,102 32,140 0,168 Z"/>
      <path class="shape-blue" d="M175,236 L288,122 C303,107 315,101 330,101 C345,101 356,110 370,124 L415,170 V236 Z"/>
    </svg>

    <h1 class="company">
      <span class="company-line1">FERNDALE</span>
      <span class="company-line2">TIDEWELL PRESS</span>
    </h1>

    <div class="person">
      <p class="person-name">Owen Marsk</p>
      <p class="person-title">Director of Sales &amp; Marketing</p>
    </div>
    <ul class="person-links">
      <li>www.ferndaletidewell.biz</li>
      <li>owen@ferndaletidewell.biz</li>
    </ul>

    <address class="contact">
      Phone: 555 014 3826<br>
      #2817 - 562 E. Harlow Ave.<br>
      Vancouver, B.C. K7P2R4 Canada
    </address>
  </section>

</main>
</body>
</html>
```